Design & Build a WordPress Website for “Coastline Stillness” (Australian Charity Rebrand)

We are a registered Australian charity currently known as Veluna Meditation Australia.

We are rebranding our public identity to “Coastline Stillness” to make the meditation practice easier to understand and more relatable for people in Australia and New Zealand.

We are looking for an experienced WordPress designer + developer to design and build a complete website that reflects:

Peace

Trust

Authentic Himalayan roots

Simplicity

Spiritual depth without being religious

Warmth, friendliness, and community feeling

This is not a corporate website. This is a meditation movement website for a non-profit organisation.

Target Market(s)

Australia and New Zealand - Age 25-65

Industry/Entity Type

Not of profit meditation organisation

Requirements
Must have
• Included in the design brief attached
Nice to have
Should not have

```html
<!DOCTYPE html>
<html lang="en">
<head>
<meta charset="utf-8">
<title>Coastline Stillness</title>
<link href="https://fonts.googleapis.com/css2?family=Marcellus&family=Poppins:wght@300;400;500;600&display=swap" rel="stylesheet">
<style>
:root{
  --ink:#1f2227;
  --muted:#555b63;
  --dark:#1b1c1f;
  --white:#ffffff;
  --sky-1:#f4f8fc;
  --sky-2:#d7e6f3;
  --sky-3:#b9d2e8;
  --line:#d9dde2;
  --card:#ffffff;
  --gold:#c9a86a;
}
*{box-sizing:border-box;margin:0;padding:0}
html,body{width:1200px;height:5272px;overflow:hidden}
body{font-family:"Poppins",sans-serif;color:var(--ink);background:var(--white);font-size:11px;line-height:1.6;position:relative}
.section{position:absolute;left:0;width:1200px}
.abs{position:absolute}
h1,h2,h3,.serif{font-family:"Marcellus",serif;font-weight:400;letter-spacing:.04em;text-transform:uppercase;color:var(--ink)}
h2{font-size:30px;line-height:1.15}
h3{font-size:14px;line-height:1.3}
p{color:var(--muted)}
.btn{display:inline-block;padding:9px 18px;font-size:10px;border-radius:4px;border:1px solid var(--dark);background:var(--dark);color:var(--white);font-weight:500}
.btn.ghost{background:var(--white);color:var(--ink);border-color:var(--line)}
ul.ticks{list-style:none;margin:10px 0}
ul.ticks li{padding-left:16px;position:relative;color:var(--muted);margin:3px 0}
ul.ticks li::before{content:"";position:absolute;left:0;top:5px;width:8px;height:8px;border-radius:50%;background:#6fae6a}

/* header */
.site-header{top:0;height:110px;background:var(--sky-1)}
.brand{left:0;width:1200px;top:22px;display:flex;justify-content:center;align-items:center;gap:10px}
.brand-dot{width:14px;height:14px;border-radius:50%;background:var(--ink)}
.brand-name{font-family:"Marcellus",serif;font-size:22px;letter-spacing:.08em;color:var(--ink)}
.lang{right:60px;top:28px;font-size:10px}
.main-nav{left:240px;top:64px;width:720px;height:30px;background:var(--white);border-radius:16px;box-shadow:0 2px 8px rgba(0,0,0,.06);display:flex;justify-content:space-around;align-items:center;font-size:8.5px;font-weight:500;text-transform:uppercase;letter-spacing:.03em}

/* hero */
.hero{top:110px;height:790px;background:linear-gradient(180deg,var(--sky-1) 0%,#e7f0f8 55%,var(--sky-2) 100%)}
.hero-photo{left:400px;top:20px;width:400px;height:440px;border-radius:24px;background:linear-gradient(180deg,#a9c3d9 0%,#7d9ab3 50%,#4d6479 100%)}
.hero h1{position:absolute;left:0;width:1200px;top:490px;text-align:center;font-size:34px;line-height:1.2}
.hero-lead{left:370px;width:460px;top:590px;text-align:center}
.hero-actions{left:0;width:1200px;top:660px;display:flex;justify-content:center;gap:10px}

/* what is */
.what{top:900px;height:470px;background:linear-gradient(180deg,var(--sky-2),#e9f1f8 60%,var(--white))}
.arch{border-radius:200px 200px 0 0;overflow:hidden}
.arch-a{left:160px;top:60px;width:140px;height:360px;background:linear-gradient(180deg,#8fa7a0,#5f6f58 55%,#3f3b33)}
.arch-b{left:310px;top:130px;width:140px;height:290px;background:linear-gradient(180deg,#cfd8de,#9fb0b5 50%,#c2704a 80%,#6b5b4d)}
.what-text{left:620px;top:60px;width:420px}
.feature-row{display:flex;gap:18px;margin:14px 0}
.feature{width:70px;text-align:center;font-size:8px;color:var(--muted)}
.feature-icon{width:26px;height:26px;border:1px solid var(--line);border-radius:50%;margin:0 auto 4px}

/* movement */
.movement{top:1370px;height:560px;background:linear-gradient(180deg,var(--white) 0%,#e6eef5 22%,#b9c9d6 45%,#7f95a6 65%,#5d7184 100%)}
.movement-title{left:0;width:1200px;top:60px;text-align:center}
.movement-photo{left:0;top:230px;width:1200px;height:330px;background:linear-gradient(180deg,rgba(255,255,255,0),rgba(120,140,160,.35))}

/* sessions */
.sessions{top:1930px;height:560px;background:var(--white)}
.sessions-text{left:140px;top:130px;width:400px}
.sessions-text h2{font-size:27px}
.session-card{top:60px;width:220px;height:420px;background:var(--card);border:1px solid var(--line);border-radius:14px;padding:10px;text-align:center}
.session-photo{height:250px;border-radius:110px 110px 8px 8px}
.session-card h3{margin:16px 0 14px}

/* together */
.together{top:2490px;height:700px;background:linear-gradient(180deg,var(--white),var(--sky-1))}
.together-head{left:0;width:1200px;top:20px;text-align:center}
.event-card{top:130px;width:205px;height:440px;background:var(--card);border:1px solid var(--line);border-radius:110px;overflow:hidden;text-align:center}
.event-photo{height:230px}
.event-label{padding:22px 20px;height:210px;display:flex;flex-direction:column;justify-content:center;align-items:center;gap:10px}
.event-icon{width:34px;height:34px;border:1px solid var(--gold);border-radius:50%}
.together-foot{left:0;width:1200px;top:595px;text-align:center}

/* building */
.building{top:3190px;height:390px;background:var(--white)}
.portrait{left:200px;top:30px;width:230px;height:300px;background:linear-gradient(160deg,#c98a3a,#a85a2a 45%,#e3d6c4 80%)}
.building-text{left:620px;top:60px;width:420px}

/* walk */
.walk{top:3580px;height:440px;background:var(--white)}
.walk-text{left:140px;top:40px;width:380px}
.walk-photo{left:668px;top:120px;width:320px;height:260px;background:linear-gradient(180deg,#e9b36a,#c67d3f 50%,#5a4a3c)}

/* learn */
.learn{top:4020px;height:520px;background:var(--white)}
.learn-head{left:0;width:1200px;top:10px;text-align:center}
.learn-card{top:100px;width:252px;height:370px;background:var(--card);border:1px solid var(--line);border-radius:8px;padding:10px}
.learn-photo{height:200px;border-radius:6px}
.learn-card h3{margin:14px 6px 8px}
.learn-card p{margin:0 6px}

/* begin */
.begin{top:4560px;height:280px;background:linear-gradient(180deg,var(--sky-2),#c6dcee)}
.begin-inner{left:0;width:1200px;top:70px;text-align:center}
.begin-actions{display:flex;justify-content:center;gap:10px;margin-top:20px}

/* footer */
.site-footer{top:4840px;height:432px;background:var(--white)}
.foot-brand{left:140px;top:60px;width:260px}
.foot-col{top:60px}
.foot-col h4{font-family:"Marcellus",serif;font-weight:400;font-size:13px;text-transform:uppercase;margin-bottom:10px;letter-spacing:.04em}
.foot-col li{list-style:none;color:var(--muted);font-size:10px;margin:3px 0}
.social{display:flex;gap:8px;margin-top:10px}
.social span{width:16px;height:16px;border-radius:50%;background:var(--dark)}
.news-field{width:150px;height:26px;border:1px solid var(--line);border-radius:4px;font-size:9px;color:var(--muted);padding:5px 8px;margin-top:8px}
.copyright{left:0;width:1200px;top:385px;text-align:center;font-size:9px;color:var(--muted);border-top:1px solid var(--line);padding-top:10px}
.to-top{left:1060px;top:390px;width:24px;height:24px;border-radius:50%;background:var(--dark)}
</style>
</head>
<body>

<header class="section site-header">
  <div class="abs brand"><span class="brand-dot"></span><span class="brand-name">COASTLINE STILLNESS</span></div>
  <div class="abs lang">EN ▾</div>
  <nav class="abs main-nav">
    <span>⌂</span><span>Coastline Stillness</span><span>Sessions &amp; Locations</span><span>Events</span><span>Quiet Ridge Project</span><span>Resources</span><span>Volunteer</span><span>Donate</span>
  </nav>
</header>

<section class="section hero">
  <div class="abs hero-photo" role="img" aria-label="Framed photo of a person meditating before misty mountains"></div>
  <h1>Simple Meditation. Deep Inner Peace.<br>For Everyday Life.</h1>
  <p class="abs hero-lead">Coastline Stillness is a gentle, natural meditation practice that helps you experience calm, clarity and emotional balance — available for modern life in Australia and New Zealand.</p>
  <div class="abs hero-actions"><span class="btn">Try a Free Meditation Session</span><span class="btn ghost">Learn What Coastline Stillness Is</span></div>
</section>

<section class="section what">
  <div class="abs arch arch-a" role="img" aria-label="Photo of a woman meditating outdoors in the mountains"></div>
  <div class="abs arch arch-b" role="img" aria-label="Photo of a person meditating on a rock facing the valley"></div>
  <div class="abs what-text">
    <h2>What is Coastline<br>Stillness?</h2>
    <p style="margin-top:12px">Coastline Stillness is a simple, effortless meditation technique taught freely by trained volunteers. It does not require concentration, chanting or changing your beliefs.</p>
    <p style="margin-top:6px">This practice comes from authentic Himalayan roots and is designed to help people:</p>
    <ul class="ticks"><li>Feel calmer and more balanced</li><li>Reduce stress and mental overload</li><li>Improve clarity and emotional wellbeing</li><li>Bring peace into daily life</li></ul>
    <div class="feature-row">
      <div class="feature"><div class="feature-icon"></div>Free to attend</div>
      <div class="feature"><div class="feature-icon"></div>Simple &amp; gentle</div>
      <div class="feature"><div class="feature-icon"></div>Suitable for all ages</div>
      <div class="feature"><div class="feature-icon"></div>Practised sitting comfortably</div>
    </div>
    <span class="btn ghost">How the Meditation Works</span>
  </div>
</section>

<section class="section movement">
  <div class="abs movement-title">
    <h2>A Meditation Movement<br>Built on Service</h2>
    <p style="margin:12px auto 0;width:480px">Coastline Stillness is offered as a service to the community. We are a registered Australian charity (Veluna Meditation Australia) dedicated to sharing meditation freely, without commercial pressure.</p>
    <div style="margin-top:14px"><span class="btn">About the Organisation</span></div>
  </div>
  <div class="abs movement-photo" role="img" aria-label="Photo of a person meditating on a mountain ridge above the clouds"></div>
</section>

<section class="section sessions">
  <div class="abs sessions-text">
    <h2>Free Meditation<br>Sessions Near You!</h2>
    <p style="margin:12px 0 16px;width:300px">We offer free guided meditation sessions across Australia and New Zealand, both in person and online. Sessions are open to everyone — beginners and experienced meditators alike.</p>
    <span class="btn ghost">Find a Session in Your Area</span>
  </div>
  <div class="abs session-card" style="left:590px">
    <div class="session-photo" role="img" aria-label="Photo of a green park building in the city" style="background:linear-gradient(180deg,#7fa36a,#4d6b45 60%,#8c8f86)"></div>
    <h3>Sydney<br>Harbour Green</h3>
    <span class="btn ghost">Book | Register</span>
  </div>
  <div class="abs session-card" style="left:825px">
    <div class="session-photo" role="img" aria-label="Photo of a modern library building" style="background:linear-gradient(180deg,#cdd8e2,#9aa6b0 55%,#6f747a)"></div>
    <h3>Auckland<br>Northgate Library</h3>
    <span class="btn ghost">Book | Register</span>
  </div>
</section>

<section class="section together">
  <div class="abs together-head">
    <h2>Meditating Together, Growing Together</h2>
    <p style="margin-top:8px">Beyond regular sessions, we organise community events and programs such as:</p>
  </div>
  <div class="abs event-card" style="left:140px">
    <div class="event-photo" role="img" aria-label="Photo of a large group meditating outdoors" style="background:linear-gradient(180deg,#c8b06a,#8a7a45)"></div>
    <div class="event-label"><h3>International<br>Yoga Day<br>Celebrations</h3></div>
  </div>
  <div class="abs event-card" style="left:365px">
    <div class="event-label"><span class="event-icon"></span><h3>Group<br>Meditation<br>Events</h3></div>
    <div class="event-photo" role="img" aria-label="Photo of people meditating together indoors" style="background:linear-gradient(180deg,#d7e2ec,#9fb6c8)"></div>
  </div>
  <div class="abs event-card" style="left:590px">
    <div class="event-photo" role="img" aria-label="Photo of a community wellbeing gathering" style="background:linear-gradient(180deg,#c99a5a,#7d5a3a)"></div>
    <div class="event-label"><h3>Community<br>Wellbeing<br>Programs</h3></div>
  </div>
  <div class="abs event-card" style="left:815px">
    <div class="event-label"><span class="event-icon"></span><h3>Special<br>Meditation<br>Workshops</h3></div>
    <div class="event-photo" role="img" aria-label="Photo of a meditation workshop in a hall" style="background:linear-gradient(180deg,#e8ddc8,#b89a72)"></div>
  </div>
  <div class="abs together-foot">
    <p>These gatherings help people connect, slow down, and feel supported.</p>
    <div style="margin-top:12px"><span class="btn">View Upcoming Events</span></div>
  </div>
</section>

<section class="section building">
  <div class="abs portrait" role="img" aria-label="Portrait painting of the tradition's spiritual teacher"></div>
  <div class="abs building-text">
    <h2>Building a Space for<br>Silence &amp; Inner Growth</h2>
    <p style="margin-top:12px">The Quiet Ridge Project is our vision for a dedicated meditation centre — a peaceful space where people can deepen meditation and reconnect with themselves.</p>
    <ul class="ticks"><li>Free meditation programs</li><li>Deeper retreats</li><li>Community learning</li><li>Long-term spiritual wellbeing</li></ul>
    <p style="margin-bottom:14px">Every contribution helps bring this vision to life.</p>
    <span class="btn ghost">Support the Quiet Ridge Project</span>
  </div>
</section>

<section class="section walk">
  <div class="abs walk-text">
    <h2>Walk the Path<br>Together</h2>
    <p style="margin-top:12px">Coastline Stillness grows through people who give their time and heart. Volunteering is a way to deepen your own practice while supporting others.</p>
    <ul class="ticks"><li>Organising sessions &amp; events</li><li>Community outreach</li><li>Event support</li><li>Administration &amp; coordination</li></ul>
    <p style="margin-bottom:14px">No experience needed — just sincerity and willingness.</p>
    <span class="btn ghost">Volunteer With Us</span>
  </div>
  <div class="abs walk-photo" role="img" aria-label="Photo of a woman meditating at sunset"></div>
</section>

<section class="section learn">
  <div class="abs learn-head">
    <h2>Learn at Your Own Pace</h2>
    <p style="margin-top:8px">Explore our growing collection of resources to support your meditation journey.</p>
  </div>
  <div class="abs learn-card" style="left:188px">
    <div class="learn-photo" role="img" aria-label="Photo of a woman meditating on a mat at home" style="background:linear-gradient(180deg,#d9c7a8,#a88e6a)"></div>
    <h3>Guided<br>Meditation Videos</h3>
    <p>Follow along with simple, calming guided sessions to practise.</p>
  </div>
  <div class="abs learn-card" style="left:474px">
    <div class="learn-photo" role="img" aria-label="Photo of a person meditating in a sunlit room" style="background:linear-gradient(180deg,#e0a95a,#9a6034)"></div>
    <h3>Articles on Stress,<br>Peace &amp; Wellbeing</h3>
    <p>Learn practical tips and insights to integrate meditation into daily life.</p>
  </div>
  <div class="abs learn-card" style="left:760px">
    <div class="learn-photo" role="img" aria-label="Photo of a teacher speaking to a seated group" style="background:linear-gradient(180deg,#e6e1d8,#b7aa96)"></div>
    <h3>Teachings from the<br>Himalayan Tradition</h3>
    <p>Explore authentic teachings adapted for modern life and wellbeing.</p>
  </div>
</section>

<section class="section begin">
  <div class="abs begin-inner">
    <h2>Begin Your Journey Inward</h2>
    <p style="margin:10px auto 0;width:520px">If life feels rushed, overwhelming, or disconnected — meditation can be a gentle way back to balance. You are warmly invited to experience Coastline Stillness.</p>
    <div class="begin-actions"><span class="btn">Try a Free Session</span><span class="btn ghost">Donate to Support the Mission</span></div>
  </div>
</section>

<footer class="section site-footer">
  <div class="abs foot-brand">
    <div style="display:flex;align-items:center;gap:8px"><span class="brand-dot"></span><span class="brand-name" style="font-size:18px">COASTLINE STILLNESS</span></div>
    <p style="margin-top:8px;font-size:9px">A project of Veluna Meditation Australia (Registered Charity)</p>
  </div>
  <div class="abs foot-col" style="left:470px">
    <h4>Useful Links</h4>
    <ul><li>About</li><li>Sessions</li><li>Events</li><li>Resources</li><li>Volunteer</li><li>Contact</li></ul>
  </div>
  <div class="abs foot-col" style="left:650px">
    <ul><li>⌖ 14 Wattle Lane, Glenhaven NSW 2156</li><li>✉ hello@coastlinestillness.org.au</li></ul>
    <div class="social"><span></span><span></span></div>
  </div>
  <div class="abs foot-col" style="left:900px">
    <h4>Newsletter</h4>
    <p style="font-size:9px">Subscribe to our newsletter</p>
    <div class="news-field">Enter email ➤</div>
  </div>
  <div class="abs copyright">© Copyright 2025 All Rights Reserved</div>
  <div class="abs to-top"></div>
</footer>

</body>
</html>
```